TOR Capital Allies LLC a High Risk Big Rewards company for Rich Young Entrepreneurs

We would like a very modern, powerful in the eyes of our customers, modern, minimalist feel, financial gain. this business card is for young Rich entrepreneurs who want to invest money into High Risk, Big Rewards Businesses. The card Should sell the business!! let your creativity go Wild! I pick most of the designers for this project because of your BOLD Designs, I would like this card to be Bold, Modern, Minimalist, use as many effects in your graphic Artist Mind, Do not let the Financial sound of this business to make you think Conservative that's the last thing we are! if you have a lot of money and you want to play a risky market call US
Updates

Project Deadline Extended
Reason: have not received, enough designs to choose 1st and second place, sure I have received over 100 designs but it seems most designers are submitting every card they have ever made before and calling it mine, please we are looking for fresh ideas please!

Target Market(s)

Private Risky Investors

Industry/Entity Type

Financial

Contact Information for Business Card

powerful in the eyes of our customers,modern, minimalist feel

Font styles to use
Other font styles liked:
• Modern feeling fonts

Requirements
Must have
• The Company Name is TOR Capital Allies LLC and it must be on the CARD
• My Name, title, Cell , email
• Dalton Fairweather G.E.D.
• Managing Member
• 404.658.1937
• dalton@torcapitalallies.example
Nice to have
• try a black thick plastic card with round corners with Dalton Fairweather GED (make sure GED is smaller than name) just on one side of the card, and my phone number with out the icons and email on the other side, this card should look like a exclusive credit card or exclusive VIP card, something you would never loose

```html
<!DOCTYPE html>
<html lang="en">
<head>
<meta charset="utf-8">
<title>TOR Capital Allies LLC — Business Card</title>
<link href="https://fonts.googleapis.com/css2?family=Archivo:wght@400;500&display=swap" rel="stylesheet">
<style>
  :root {
    --backdrop: #d6d6d4;
    --card: #e7e7e5;
    --ink: #262626;
    --band: #2b2b2b;
    --accent: #e2716c;
    --accent-text: #d8443a;
    --paper-text: #f2f2f2;
    --art-dark: #4a3a37;
    --art-mid: #7a7a7b;
    --art-light: #c2c2c1;
  }
  * { box-sizing: border-box; margin: 0; padding: 0; }
  html, body { width: 1200px; height: 1200px; overflow: hidden; }
  body {
    background: var(--backdrop);
    font-family: "Archivo", Arial, sans-serif;
    color: var(--ink);
    position: relative;
  }
  .card {
    position: absolute;
    top: 250px;
    width: 460px;
    height: 700px;
    background: var(--card);
    box-shadow: 0 6px 18px rgba(0,0,0,0.18);
    overflow: hidden;
  }
  .card--front { left: 90px; }
  .card--back { left: 650px; }

  .company-band {
    position: absolute;
    left: 90px;
    top: 105px;
    width: 280px;
    height: 42px;
    background: var(--band);
    color: var(--paper-text);
    font-size: 15px;
    letter-spacing: 2.4px;
    display: flex;
    align-items: center;
    justify-content: center;
    text-transform: uppercase;
  }
  .portrait-art {
    position: absolute;
    left: 100px;
    top: 180px;
    width: 260px;
    height: 330px;
    border-radius: 4px;
    background: radial-gradient(ellipse at 45% 35%, var(--art-mid) 0%, var(--art-dark) 70%);
  }
  .holder {
    position: absolute;
    left: 0;
    right: 0;
    top: 600px;
    text-align: center;
  }
  .holder-name {
    font-size: 17px;
    letter-spacing: 2px;
    text-transform: uppercase;
    font-weight: 500;
  }
  .holder-name .credential {
    color: var(--accent-text);
    font-size: 14px;
    letter-spacing: 1px;
  }
  .holder-title {
    margin-top: 10px;
    font-size: 13px;
    letter-spacing: 1.8px;
    text-transform: uppercase;
    font-weight: 500;
  }

  .contact-block {
    position: absolute;
    left: 62px;
    top: 320px;
    width: 360px;
  }
  .phone-row { display: flex; height: 38px; }
  .phone-icon {
    width: 68px;
    background: var(--accent);
    display: flex;
    align-items: center;
    justify-content: center;
  }
  .phone-number {
    flex: 1;
    margin-left: 4px;
    background: var(--band);
    color: var(--paper-text);
    font-size: 16px;
    letter-spacing: 2px;
    display: flex;
    align-items: center;
    justify-content: center;
  }
  .email {
    margin-top: 8px;
    font-size: 15px;
    letter-spacing: 1.6px;
    text-transform: uppercase;
    padding-bottom: 8px;
    border-bottom: 1.5px solid var(--ink);
    white-space: nowrap;
  }
</style>
</head>
<body>
  <section class="card card--front">
    <div class="company-band">TOR Capital Allies LLC</div>
    <div class="portrait-art" role="img" aria-label="Flat illustration of a bearded man in a dark hat with a pink band, casting a long grey shadow"></div>
    <div class="holder">
      <p class="holder-name">Dalton Fairweather <span class="credential">G.E.D</span></p>
      <p class="holder-title">Managing Member</p>
    </div>
  </section>

  <section class="card card--back">
    <div class="contact-block">
      <div class="phone-row">
        <div class="phone-icon">
          <svg width="16" height="20" viewBox="0 0 16 20" aria-hidden="true">
            <path d="M4 1 L7 5 L5 7 Q6 11 9 14 L11 12 L15 15 L13 18 Q7 18 4 12 Q1 6 4 1 Z" fill="#ffffff"/>
          </svg>
        </div>
        <div class="phone-number">404.658.1937</div>
      </div>
      <p class="email">dalton@torcapitalallies.example</p>
    </div>
  </section>
</body>
</html>
```